we need a business card design for a professional painting business. This company has been up and going for about ten years. However it needs an new logo. we want this business card to be modern eye catching and easy to read. I currently have been looking for VP logos but can not find one that suits our needs. This Design should be Our start to a new beginning.
Industry/Entity Type
Painting
Contact Information for Business Card
Varesko Painting Inc.
Licensed & Insured
Tomas Varesko
Phone(631)384-4562
Fax (555) 846-3021
E-mail vareskopaintinginc@mailorbit.test
Requirements
Must have
- a new logo with  VP and i would like it to be in black and white.
i would also like the front to be a solid black with the logo only and then the back to have the information.

```html
<!DOCTYPE html>
<html lang="en">
<head>
<meta charset="utf-8">
<title>Varesko Painting Inc. – Business Card</title>
<link rel="stylesheet" href="https://fonts.googleapis.com/css2?family=Almendra&family=Pinyon+Script&display=swap">
<style>
  :root {
    --ink: #000000;
    --paper: #ffffff;
    --script: "Pinyon Script", cursive;
    --text: "Almendra", serif;
  }
  html, body {
    margin: 0;
    padding: 0;
    width: 1053px;
    height: 1200px;
    overflow: hidden;
    background: var(--paper);
  }
  .canvas {
    position: relative;
    width: 1053px;
    height: 1200px;
  }
  .card {
    position: absolute;
    background: var(--ink);
    color: var(--paper);
    overflow: hidden;
  }
  .card--front {
    left: 3px;
    top: 3px;
    width: 1042px;
    height: 576px;
    display: flex;
    align-items: center;
    justify-content: center;
  }
  .brand {
    display: flex;
    align-items: center;
    gap: 22px;
  }
  .brand__dot {
    width: 34px;
    height: 34px;
    border-radius: 50%;
    background: var(--paper);
    flex: none;
  }
  .brand__name {
    font-family: var(--text);
    font-weight: 400;
    font-size: 56px;
    line-height: 1;
    color: var(--paper);
    white-space: nowrap;
  }
  .card--back {
    left: 6px;
    top: 620px;
    width: 1042px;
    height: 575px;
  }
  .company-name {
    position: absolute;
    left: 30px;
    top: 50px;
    margin: 0;
    font-family: var(--script);
    font-weight: 400;
    font-size: 104px;
    line-height: 100px;
    color: var(--paper);
  }
  .company-name__line {
    display: block;
    white-space: nowrap;
  }
  .company-name__line--second {
    padding-left: 14px;
  }
  .divider {
    position: absolute;
    left: 39px;
    top: 262px;
    width: 608px;
    height: 3px;
    background: var(--paper);
  }
  .tagline {
    position: absolute;
    left: 40px;
    top: 282px;
    margin: 0;
    font-family: var(--text);
    font-size: 50px;
    letter-spacing: 5px;
    word-spacing: 8px;
    white-space: nowrap;
  }
  .contact {
    position: absolute;
    left: 48px;
    top: 365px;
    margin: 0;
    padding: 0;
    list-style: none;
    font-family: var(--text);
    font-size: 36px;
    line-height: 52px;
    letter-spacing: 2px;
    white-space: nowrap;
  }
</style>
</head>
<body>
<main class="canvas">
  <section class="card card--front" aria-label="Card front">
    <div class="brand">
      <span class="brand__dot"></span>
      <span class="brand__name">Varesko Painting Inc.</span>
    </div>
  </section>

  <section class="card card--back" aria-label="Card back">
    <h1 class="company-name">
      <span class="company-name__line">Varesko</span>
      <span class="company-name__line company-name__line--second">Painting Inc</span>
    </h1>
    <div class="divider"></div>
    <p class="tagline">Licensed &amp; Insured Tomas Varesko</p>
    <ul class="contact">
      <li class="contact__item">Phone(555)217-9083</li>
      <li class="contact__item">Fax (555) 846-3021</li>
      <li class="contact__item">E-mail: vareskopaintinginc@mailorbit.test</li>
    </ul>
  </section>
</main>
</body>
</html>
```